Re-Brand of TindelMox along with a new website design

TindelMox Ltd are a software & database development company using technologies such as PHP, C#, HTML, JQuery, Flex, AS3, MySQL, Oracle, MSSQL. We like to target all types of business from small to large.

We are great at coding but rubbish at design so thats where we need your help!

We want a complete re-brand of TindelMox including logo, website design, and business cards.

We would like a design that is clean but other than that, please feel free to be creative.

****Logo****
We are looking for a logo that appears professional but with a splash of colour that indicates a creative side. Please see below some logos that we like the look of:

We like this one because it has a nice simple and clear font for the name of the company but also an icon which is colourful and stands out. http://markvault.example/2013/03/brivelo/

We like this one because it is very clean, simple and again very clear. http://markvault.example/2013/03/quantorels/

http://markvault.example/2013/03/tide-lamp/
http://markvault.example/2013/02/velmorin/
http://markvault.example/2013/01/art-gallery-tarnwick/

As you will see from all of these examples, the font is very clear but there is always a graphic representing the company too. This is what we like.

****Website****
These are some of the examples of websites we like:
https://www.zestrune.example/
https://www.chatterlane.example/home
http://www.haldenimagery.example/
http://www.vistor.example/
http://quillbay.example/
https://www.usebriefnest.example/personal-intros
http://www.marmotpanel.example/

The current site can be found at tindelmox.example.uk

Reason: We have extended the deadline of the project by 5 days as I realise the original deadline was very tight.

Software

Requirements
Must have
• Website must have the following pages
Home
Services
Projects
About Us
Contact Us

```html
<!DOCTYPE html>
<html lang="en">
<head>
<meta charset="utf-8">
<title>TindelMox – Web, Software &amp; Database Development</title>
<link href="https://fonts.googleapis.com/css2?family=Questrial&display=swap" rel="stylesheet">
<style>
:root{
  --green:#8dc63f;
  --green-dark:#79b12c;
  --green-deep:#6aa023;
  --ink:#2b2b2b;
  --body:#8a8a8a;
  --rule:#e2e2e2;
  --band:#ececec;
  --white:#ffffff;
}
*{margin:0;padding:0;box-sizing:border-box}
html,body{width:848px;height:1200px;overflow:hidden;background:var(--white)}
body{font-family:"Questrial",sans-serif;color:var(--ink)}
.page{position:relative;width:848px;height:1200px;overflow:hidden}
.abs{position:absolute}

.top-bar{left:0;top:0;width:848px;height:5px;background:var(--green)}
.header{left:0;top:5px;width:848px;height:115px;background:var(--white)}
.brand{left:98px;top:60px;display:flex;align-items:center;gap:10px}
.brand-dot{width:30px;height:30px;border-radius:50%;background:var(--green)}
.brand-name{font-size:31px;color:var(--green);letter-spacing:-0.5px;line-height:1}
.nav{left:347px;top:71px;display:flex;gap:0;font-size:12px;letter-spacing:0.2px}
.nav a{color:var(--ink);text-decoration:none;margin-right:29px}
.nav a.current{color:var(--green)}

.hero-band{left:0;top:120px;width:848px;height:196px;background:#e4e4e4;
  background-image:radial-gradient(#d6d6d6 1px,transparent 1.2px);background-size:5px 5px}
.green-band{left:0;top:316px;width:848px;height:127px;background:var(--green)}
.hero-shadow{left:120px;top:400px;width:610px;height:20px;border-radius:50%;
  background:radial-gradient(ellipse at center,rgba(40,70,10,.45),rgba(40,70,10,0) 70%)}
.hero-card{left:92px;top:139px;width:664px;height:265px;background:var(--white);border-radius:4px;overflow:hidden;box-shadow:0 1px 3px rgba(0,0,0,.15)}
.hero-photo{position:absolute;left:0;top:0;width:380px;height:265px;
  background:linear-gradient(90deg,#d9e1e8 0%,#eef2f5 55%,rgba(255,255,255,0) 100%)}
.hero-mark{position:absolute;left:475px;top:31px;width:36px;height:36px;border-radius:50%;background:var(--green)}
.hero-title{position:absolute;left:375px;top:78px;font-size:28px;letter-spacing:.5px;white-space:nowrap}
.hero-title span{color:var(--green)}
.hero-text{position:absolute;left:382px;top:119px;width:252px;font-size:8.4px;line-height:12.8px;color:#555;text-align:justify}
.btn{position:absolute;left:556px;top:215px;width:79px;height:22px;background:var(--green);color:var(--white);font-size:10px;display:flex;align-items:center;justify-content:center}
.arrow{width:38px;height:58px;background:var(--white);top:240px;display:flex;align-items:center;justify-content:center}
.arrow.prev{left:63px;border-radius:29px 0 0 29px}
.arrow.next{left:756px;border-radius:0 29px 29px 0}

.services{left:0;top:443px;width:848px;height:427px;background:#f1f1f1}
.section-rule{left:0;top:483px;width:848px;height:1px;background:var(--rule)}
.section-title{width:848px;left:0;text-align:center;font-size:16px;letter-spacing:.5px}
.section-title span{color:var(--green)}
.col-rule{width:1px;height:325px;top:500px;background:var(--rule)}
.service{width:222px}
.service-head{display:flex;align-items:center;gap:9px;font-size:11.5px;height:26px}
.service-head svg{flex:none}
.service p{font-size:6.9px;line-height:9.9px;color:var(--body);text-align:justify;margin-left:37px;width:173px}
.service p + p{margin-top:0}
.service p.gap{margin-top:9.9px}
.band-end{left:0;top:870px;width:848px;height:1px;background:#dedede}
.pager{left:406px;top:850px;display:flex;gap:3px}
.pager i{width:10px;height:10px;border-radius:50%;background:#666;display:block}
.pager i.on{background:var(--green)}

.partners-band{left:0;top:975px;width:848px;height:53px;background:linear-gradient(#ececec,#f7f7f7)}
.partners{left:122px;top:932px;display:flex;gap:6px;align-items:center}
.partner{height:64px;display:flex;align-items:center;justify-content:center;font-size:13px;color:#444;background:var(--white)}

.footer{left:0;top:1028px;width:848px;height:140px;background:var(--green)}
.footer-base{left:0;top:1168px;width:848px;height:32px;background:var(--green-dark)}
.f-col{font-size:8.4px;line-height:14px;color:var(--white)}
.social{left:441px;display:flex;align-items:center}
.social i{width:25px;height:25px;border-radius:50%;background:var(--white);display:block}
.social span{font-size:10px;color:var(--white);margin-left:35px}
.subscribe{left:602px;top:1061px;width:154px;height:77px;background:var(--green-deep);box-shadow:0 1px 3px rgba(0,0,0,.25)}
.subscribe h3{position:absolute;left:51px;top:9px;font-weight:normal;font-size:16px;color:var(--white)}
.subscribe p{position:absolute;left:53px;top:30px;width:96px;font-size:5.6px;line-height:8px;color:#e8f5d6}
.subscribe .field{position:absolute;left:11px;top:54px;width:113px;height:13px;background:var(--white)}
.subscribe .go{position:absolute;left:130px;top:54px;width:14px;height:14px;border-radius:50%;background:#e0efcc;font-size:6px;color:var(--green-deep);display:flex;align-items:center;justify-content:center}
.copyright{left:0;top:1178px;width:848px;text-align:center;font-size:9px;color:var(--white)}
</style>
</head>
<body>
<div class="page">
  <div class="abs top-bar"></div>
  <header class="abs header"></header>
  <div class="abs brand"><div class="brand-dot"></div><div class="brand-name">TINDELMOX</div></div>
  <nav class="abs nav">
    <a class="current" href="#">HOME</a><a href="#">WHAT WE DO</a><a href="#">PROJECTS</a><a href="#">ABOUT US</a><a href="#">CONTACT US</a>
  </nav>

  <div class="abs hero-band"></div>
  <div class="abs green-band"></div>
  <div class="abs hero-shadow"></div>
  <div class="abs arrow prev"><svg width="12" height="18" viewBox="0 0 12 18"><path d="M10 2 3 9l7 7" fill="none" stroke="#555" stroke-width="2"/></svg></div>
  <div class="abs arrow next"><svg width="12" height="18" viewBox="0 0 12 18"><path d="M2 2l7 7-7 7" fill="none" stroke="#555" stroke-width="2"/></svg></div>
  <section class="abs hero-card">
    <div class="hero-photo" role="img" aria-label="Photo of two colleagues looking at a phone beside a laptop in a bright office"></div>
    <div class="hero-mark"></div>
    <h1 class="hero-title" style="font-weight:normal">Welcome to <span>TindelMox</span></h1>
    <div class="hero-text">
      <p>if you are looking for web, software, or IT services that really deliver but you don't want to pay over the odds then TindelMox is the right team for you.</p>
      <p>Based in Brackwell our clients are both local, national, both large and small. You may be a start-up business in need of a 'get me up and running quickly' website, or a multi-million pound brand looking for an all singing, all dancing bespoke app.</p>
    </div>
    <div class="btn">Read More</div>
  </section>

  <section class="abs services"></section>
  <h2 class="abs section-title" style="top:457px;font-weight:normal">WHAT <span>WE DO ?</span></h2>
  <div class="abs section-rule"></div>
  <div class="abs col-rule" style="left:318px"></div>
  <div class="abs col-rule" style="left:548px"></div>

  <div class="abs service" style="left:96px;top:510px">
    <div class="service-head"><svg width="27" height="27" viewBox="0 0 28 28"><circle cx="14" cy="14" r="12" fill="none" stroke="#8dc63f" stroke-width="3"/><path d="M2 14h24M14 2v24M5 7h18M5 21h18" stroke="#8dc63f" stroke-width="2"/><ellipse cx="14" cy="14" rx="6" ry="12" fill="none" stroke="#8dc63f" stroke-width="2"/></svg>Website Design &amp; Development</div>
    <p style="margin-top:11px">Your website is a representation of who you are or what your business stands for.If you feel your website could better show off who you are and what you do TindelMox is the right team for you.You will work with a team that will find out exactly what you want, deliver quickly and not break the bank.</p>
    <p>Our team would be happy to talk over your ideas at a time and venue that is convenient for you so get in touch by clicking here.</p>
  </div>
  <div class="abs service" style="left:326px;top:510px">
    <div class="service-head"><svg width="27" height="24" viewBox="0 0 28 24"><rect x="2" y="2" width="24" height="15" rx="1" fill="none" stroke="#8dc63f" stroke-width="2.5"/><path d="M11 17v3h6v-3M8 22h12" stroke="#8dc63f" stroke-width="2.5" fill="none"/></svg>Rich Internet Applications</div>
    <p style="margin-top:11px">You may be asking yourself, "what the heck is a Rich Internet Application..?" The chances are you play with one every day. If you have ever used Sheetwise Docs then you know what we are talking about.</p>
    <p>A Rich Internet Application is all about offering your clients a more engaging and immersive experience and in turn, you will receive greater customer loyalty and efficiency.so get in touch by clicking here.</p>
  </div>
  <div class="abs service" style="left:556px;top:510px">
    <div class="service-head"><svg width="27" height="26" viewBox="0 0 28 26"><rect x="7" y="1" width="14" height="24" rx="2" fill="none" stroke="#8dc63f" stroke-width="2.5"/><path d="M7 5h14M7 20h14" stroke="#8dc63f" stroke-width="1.5"/></svg>Mobile &amp; Tablet Applications</div>
    <p style="margin-top:11px">If you are sitting on the next great idea for a mobile or tablet app TindelMox has all the experience you need.</p>
    <p>You will work with a team who are able to get your idea onto all of the major mobile platforms including Orbitphone, Slatepad, Droidane and Panesoft.</p>
  </div>

  <div class="abs service" style="left:96px;top:683px">
    <div class="service-head"><svg width="27" height="27" viewBox="0 0 28 28"><rect x="10" y="1" width="8" height="6" fill="#8dc63f"/><path d="M14 7v6M5 13h18M5 13v7M14 13v7M23 13v7" stroke="#8dc63f" stroke-width="2" fill="none"/><rect x="2" y="20" width="6" height="6" fill="#8dc63f"/><rect x="11" y="20" width="6" height="6" fill="#8dc63f"/><rect x="20" y="20" width="6" height="6" fill="#8dc63f"/></svg>Enterprise Development</div>
    <p style="margin-top:11px">If you are sitting on the next great idea for a mobile or tablet app TindelMox has all the experience you need.</p>
    <p>You will work with a team who are able to get your idea onto all of the major mobile platforms including Orbitphone, Slatepad, Droidane and Panesoft.</p>
    <p class="gap">Sound interesting? Get in contact here and lets have a chat about your ideas.</p>
  </div>
  <div class="abs service" style="left:326px;top:683px">
    <div class="service-head"><svg width="28" height="22" viewBox="0 0 28 22"><path d="M7 20a6 6 0 0 1-1-12 8 8 0 0 1 15-1 6 6 0 0 1 1 13z" fill="#8dc63f"/><path d="M14 17V9M10 12l4-4 4 4" stroke="#fff" stroke-width="2" fill="none"/></svg>Database Development</div>
    <p style="margin-top:11px">The information you have as a business is crucial to the way your business runs and the decisions you make. Having a professional and scalable database structure that ensures you can understand your business from all aspects is essential and something which TindelMox can help you with.</p>
    <p class="gap">Contact us here to get a free no obligation consultation.</p>
  </div>
  <div class="abs service" style="left:556px;top:683px">
    <div class="service-head"><svg width="26" height="26" viewBox="0 0 26 26"><circle cx="13" cy="13" r="10" fill="none" stroke="#8dc63f" stroke-width="5" stroke-dasharray="4 3.85"/><circle cx="13" cy="13" r="7" fill="#8dc63f"/><circle cx="13" cy="13" r="3" fill="#f1f1f1"/></svg>Database Reporting</div>
    <p style="margin-top:11px">If you have an existing database structure and you would like to create some more extensive reports to understand your business in a greater way TindelMox has the skill and experience you need.</p>
    <p class="gap">If you would like to get in contact click here</p>
  </div>

  <div class="abs pager"><i class="on"></i><i></i><i></i></div>
  <div class="abs band-end"></div>

  <h2 class="abs section-title" style="top:888px;font-weight:normal">OUE <span>PROJECT PARTNER</span></h2>
  <div class="abs partners-band"></div>
  <div class="abs partners">
    <div class="partner" style="width:102px;background:#ededed">Dashline</div>
    <div class="partner" style="width:82px;background:transparent">Wayfold</div>
    <div class="partner" style="width:88px;background:transparent">Postboard</div>
    <div class="partner" style="width:102px;background:#ededed">Mailcrest</div>
    <div class="partner" style="width:116px;background:transparent">Bizkit Tools</div>
    <div class="partner" style="width:58px;background:#8a1f5a;color:#fff;font-size:9px">Harlow</div>
  </div>

  <footer class="abs footer"></footer>
  <div class="abs f-col" style="left:92px;top:1057px">Home<br>What We Do<br>Projects<br>About Us<br>Contact Us</div>
  <div class="abs f-col" style="left:205px;top:1057px">Support<br>Legal Notice<br>Terms &amp; Conditions<br>Privacy Policy<br>FAQS</div>
  <div class="abs f-col" style="left:317px;top:1057px">Telephone<br>01632 960 418<br>Email<br>contact@tindelmox.example.uk<br>Address<br>48 Fernhollow Lane<br>Brackwell Shire, BK4 9TR</div>
  <div class="abs social" style="top:1060px"><i></i><span style="margin-left:35px">Chirpline</span></div>
  <div class="abs social" style="top:1094px"><i></i><span style="margin-left:38px">Facepost</span></div>
  <div class="abs social" style="top:1126px"><i></i><span style="margin-left:38px">RSS Feeds</span></div>
  <div class="abs subscribe">
    <svg style="position:absolute;left:12px;top:14px" width="34" height="30" viewBox="0 0 34 30"><path d="M4 12 17 3l13 9v14H4z" fill="none" stroke="#fff" stroke-width="2"/><path d="M4 12l13 9 13-9" fill="none" stroke="#fff" stroke-width="2"/><circle cx="7" cy="25" r="5" fill="#fff"/><path d="M4.5 25l2 2 3-4" stroke="#6aa023" stroke-width="1.5" fill="none"/></svg>
    <h3>Subscribe</h3>
    <p>Lorem Ipsum is simply dummy text of the printing and typesetting</p>
    <div class="field"></div>
    <div class="go">Go</div>
  </div>
  <div class="abs footer-base"></div>
  <div class="abs copyright">Copyright © 2013 TindelMox &nbsp;- All rights reserved.</div>
</div>
</body>
</html>
```